Web Design Project

Full website, similar _function_ to http://www.kindlarkfund.com/
You can not only make charities, but also communicate social or environmental problems by posting them on the website.
I need a full layout design, right now I am using a slightly changed bootstrap. View attached file "basic css" for current containers layout
Including front page, static text page (SEO), show listing page and content page, all the same look and feel. Dont focus to hard on the charity part...

Logo will be needed:
The URL - also the Logo - is Wutbrand.de - that is German for "Outcry" - so working with a "!" makes prob. sense, like Wutbrand!de or so... (EXTRA)

Colour Scheme:
I do not have a colour scheme, but I alreay think "Red URL with green elements" would be nice - that means please give me some other ideas ... I am not a designer, right?! :)

NO CODING NEEDED

Reason: I just got too few designs, some nice with it, though - I will clarify my needs new so it will be easier to reply with suggestions! :)

Target Market(s)

People who want to do charity and help other people

Industry/Entity Type

Charity

Requirements
Must have
• responsive design (tablet, smartphone)
static frame header (like here at pixelhive)

```html
<!DOCTYPE html>
<html lang="en">
<head>
<meta charset="utf-8">
<title>Wutbrand.de – Charity Community</title>
<link rel="stylesheet" href="https://fonts.googleapis.com/css2?family=Archivo+Narrow:wght@400;700&family=Open+Sans:wght@400;600&display=swap">
<style>
:root{
  --crimson:#b0102f;
  --green:#8ccc0c;
  --green-dark:#6fae05;
  --page:#ececec;
  --panel:#ffffff;
  --text:#8a8a8a;
  --text-dark:#555555;
  --rule-dark:#555555;
  --box:#eeeeee;
  --footer-top:#4c4c4c;
  --footer-bottom:#2e2e2e;
}
*{box-sizing:border-box;margin:0;padding:0}
html,body{width:793px;height:1200px;overflow:hidden}
body{position:relative;background:var(--page);font-family:"Archivo Narrow",Arial,sans-serif;color:var(--text)}
.abs{position:absolute}
.topbar{left:0;top:0;width:793px;height:33px;background:var(--crimson);color:#fff;font-size:11px}
.topbar nav a{position:absolute;top:12px;color:#fff;text-decoration:none}
.topbar .call{position:absolute;right:75px;top:12px;display:flex;align-items:center;gap:6px}
.header{left:0;top:33px;width:793px;height:75px;background:#fff;box-shadow:0 2px 4px rgba(0,0,0,.08)}
.logo{left:67px;top:45px;display:flex;align-items:center;gap:8px;color:var(--crimson);font-weight:700;font-size:20px}
.logo i{display:block;width:30px;height:30px;border-radius:50%;background:var(--crimson)}
.search{left:538px;top:70px;display:flex}
.search .field{width:130px;height:20px;border:1px solid #ccc;border-right:0;font-size:8px;font-style:italic;color:#777;padding:5px 6px;background:#fff;box-shadow:inset 0 1px 2px rgba(0,0,0,.15)}
.btn{background:linear-gradient(#a5dd1c,var(--green-dark));color:#fff;font-size:10px;display:flex;align-items:center;justify-content:center}
.search .btn{width:51px;height:20px}
.panel{left:54px;top:108px;width:683px;height:932px;background:var(--panel)}
.crumb{left:70px;top:124px;font-size:10px}
.hero{left:67px;top:147px;width:653px;height:300px;background:linear-gradient(135deg,#7d8a92 0%,#b9b6ad 40%,#6c7784 75%,#3d4651 100%)}
.hero-card{left:85px;top:263px;width:276px;height:162px;background:rgba(60,60,60,.6);border-radius:4px;color:#fff;padding:20px 12px}
.hero-card h1{font-size:20px;line-height:24px;font-weight:700}
.hero-card p{font-size:9.5px;line-height:13px;margin-top:3px}
.hero-card .btn{position:absolute;left:13px;top:117px;width:99px;height:21px;border-radius:3px;font-size:12px}
.hero-arrows{left:329px;top:386px}
.side-title{left:70px;width:200px;border-top:3px solid var(--crimson);padding-top:8px;color:var(--crimson);font-size:13px}
.blog-list{left:70px;top:519px;list-style:none}
.blog-list li{display:flex;align-items:center;height:37.5px}
.thumb{width:35px;height:30px;margin-right:6px}
.blog-list span{font-size:10px;color:#666;border-bottom:1px dotted #ccc;padding-bottom:2px}
.quote{left:70px;width:200px;display:flex;gap:9px}
.quote .face{width:56px;height:52px;flex:none}
.quote h3{font-size:10px;color:#333;font-weight:700;margin-top:6px}
.quote p{font-size:10px;line-height:15px;margin-top:4px}
.main-title{left:287px;top:472px;color:var(--crimson);font-size:23px;font-weight:400}
.feature{left:289px;top:524px;width:432px;height:133px;background:linear-gradient(120deg,#3b3f48 0%,#8a8d90 45%,#d9d6cf 70%,#c9b23a 100%)}
.intro{left:289px;top:670px;width:420px;font-size:10px;line-height:15px}
.more{left:646px;top:711px;display:flex;align-items:center;gap:7px;color:var(--crimson);font-size:12px}
.col{width:212px;border-top:3px solid var(--rule-dark);padding-top:10px}
.col h2{font-size:12.5px;font-weight:400;color:var(--text-dark)}
.col p{font-size:10px;line-height:15px;margin-top:25px;padding-left:2px}
.col .form{display:flex;margin-top:14px;padding-left:2px}
.col .field{width:129px;height:20px;border:1px solid #ccc;border-right:0;font-size:8px;font-style:italic;color:#777;padding:5px 6px;box-shadow:inset 0 1px 2px rgba(0,0,0,.15)}
.col .btn{width:51px;height:20px}
.links-box{left:287px;top:895px;width:433px;height:95px;background:var(--box);padding:14px 21px}
.links-box h2{font-size:12px;font-weight:400;color:var(--text-dark)}
.links-box ul{position:absolute;top:38px;list-style:none;font-size:9.5px}
.links-box li{height:16.5px;padding-left:14px;position:relative}
.links-box li::before{content:"";position:absolute;left:0;top:2px;border-left:6px solid #888;border-top:3.5px solid transparent;border-bottom:3.5px solid transparent}
.footer{left:0;top:1040px;width:793px;height:160px;background:linear-gradient(var(--footer-top),var(--footer-bottom));color:#fff;font-family:"Open Sans",Arial,sans-serif}
.footer h2{position:absolute;top:11px;font-size:12.5px;font-weight:400}
.footer ul{position:absolute;top:41px;list-style:none;font-size:8.5px}
.footer ul li{height:17px}
.footer ul li::before{content:"→ ";font-size:7px}
.footer .about{position:absolute;left:197px;top:44px;width:318px;font-size:8px;line-height:16px}
.footer .contact{position:absolute;left:545px;top:39px;font-size:8.5px}
.footer .contact div{display:flex;align-items:center;gap:8px;height:24px}
.footer .rule{position:absolute;left:54px;top:117px;width:683px;border-top:1px solid #555}
.footer .copy{position:absolute;left:68px;top:129px;font-size:10px}
</style>
</head>
<body>
<header class="abs topbar">
  <nav>
    <a style="left:67px" href="#">Home</a>
    <a style="left:117px" href="#">Blog</a>
    <a style="left:163px" href="#">Community</a>
    <a style="left:230px" href="#">About us</a>
  </nav>
  <div class="call">
    <svg width="15" height="11" viewBox="0 0 15 11"><path d="M1 4 Q7.5 -1 14 4 L12 5.5 L10 4 L10 3 Q7.5 2 5 3 L5 4 L3 5.5Z M4 6 L11 6 L12 10 L3 10Z" fill="#fff"/></svg>
    Call Toll Free: ( 4120 ) 5530 918
  </div>
</header>
<div class="abs header"></div>
<div class="abs logo"><i></i>Wutbrand.de</div>
<div class="abs search"><div class="field">keywords</div><div class="btn">Search</div></div>

<main class="abs panel"></main>
<div class="abs crumb">Charity Community /</div>

<section class="abs hero" role="img" aria-label="Photo of a marathon runner on a sunny town street"></section>
<div class="abs hero-card">
  <h1>Charity clearing-house opens for marathon hopefuls</h1>
  <p>Nullam elit nisi, sollicitudin in venenatis id, varius et turpis. Class aptent taciti sociosqu ad</p>
  <div class="btn">Donate NOW</div>
</div>
<svg class="abs hero-arrows" width="20" height="12" viewBox="0 0 20 12"><path d="M7 1 L1 6 L7 11Z M12 1 L18 6 L12 11Z" fill="#fff"/></svg>

<h2 class="abs side-title" style="top:477px">READ OUR BLOG</h2>
<ul class="abs blog-list">
  <li><div class="thumb" role="img" aria-label="Cyclists photo" style="background:#6d7a55"></div><span>Bike for charity in 2013</span></li>
  <li><div class="thumb" role="img" aria-label="Team photo" style="background:#5b5a45"></div><span>Work at a charity?</span></li>
  <li><div class="thumb" role="img" aria-label="Fundraiser photo" style="background:#6f9a4c"></div><span>Raising money or giving to charity?</span></li>
  <li><div class="thumb" role="img" aria-label="Event photo" style="background:#3f5a3a"></div><span>Brighten up your Blue Monday</span></li>
  <li><div class="thumb" role="img" aria-label="Sponsors photo" style="background:#5a4a48"></div><span>Sponsor a friend</span></li>
  <li><div class="thumb" role="img" aria-label="Mascot photo" style="background:#b04a1c"></div><span>Become a charity member</span></li>
</ul>

<h2 class="abs side-title" style="top:772px">WHAT THEY SAY</h2>
<div class="abs quote" style="top:819px">
  <div class="face" role="img" aria-label="Portrait of the sponsor" style="background:#8a6a58"></div>
  <div><h3>Tom HARLOW - Sponsor</h3><p>Lorem ipsum dolor sit amet, consecte-tur adipisicing elit, sed do eiusmod tempor incididunt ut labore et dolore</p></div>
</div>
<div class="abs quote" style="top:913px">
  <div class="face" role="img" aria-label="Portrait of the charity member" style="background:#b08a70"></div>
  <div><h3>Mia VANCE - Chiarity Member</h3><p>Lorem ipsum dolor sit amet, consecte-tur adipisicing elit, sed do eiusmod tempor incididunt ut labore et dolore magna aliqua.</p></div>
</div>

<h1 class="abs main-title">Enjoy a genuine difference</h1>
<div class="abs feature" role="img" aria-label="Photo of smiling cyclists in helmets at a charity ride"></div>
<p class="abs intro">This innovative, market-leading Managed Service programme is specifically designed to help Trusts achieve their spending cuts, while providing the best temporary workforce possible, and thus the best patient care.</p>
<div class="abs more">Read More
  <svg width="14" height="14" viewBox="0 0 14 14"><circle cx="7" cy="7" r="7" fill="var(--crimson)"/><path d="M5.5 3.8 L9.5 7 L5.5 10.2Z" fill="#fff"/></svg>
</div>

<section class="abs col" style="left:287px;top:745px">
  <h2>DONATE TO CHARITY</h2>
  <p>We were thrilled to receive an Giving Partners Award last week for our free text donation service.</p>
  <div class="form"><div class="field">charity's name</div><div class="btn">Search</div></div>
</section>
<section class="abs col" style="left:515px;top:745px;width:205px">
  <h2>START FUNDRAISING</h2>
  <p>We were thrilled to receive an Giving Partners Award last week for our free text donation service.</p>
  <div class="form"><div class="field">project's name</div><div class="btn">Search</div></div>
</section>

<section class="abs links-box">
  <h2>WUTBRAND.DE</h2>
  <ul style="left:24px"><li>Charity</li><li>Donate to a Friend</li><li>Help your kind</li></ul>
  <ul style="left:156px"><li>Marathon against Poverty</li><li>Become a Charity Member</li><li>Work for Charity?</li></ul>
  <ul style="left:310px"><li>Start Fundraising</li><li>Our Latest Auctions</li><li>Terms of Use</li></ul>
</section>

<footer class="abs footer">
  <h2 style="left:68px">Navigation</h2>
  <ul style="left:68px"><li>Home</li><li>Our Latest Products</li><li>Terms of Use</li><li>Privacy Policy</li></ul>
  <h2 style="left:197px">About Wutbrand.de</h2>
  <p class="about">"Nullam sagittis, libero imperdiet facilisis vestibulum, tellus dui pharetra risus, nec conse quat leo lectus at massa. Aenean massa nisi, faucibus eu facilisis eget, pulvinar sit amet orci. Morbi dolor nisi, laoreet at luctus ut, convallis id elit. Duis porta libero non mi auctor non ullamcorper justo tempus. In hendrerit convallis odio, sit amet."</p>
  <h2 style="left:542px">Get in touch with us</h2>
  <div class="contact">
    <div><svg width="14" height="12" viewBox="0 0 14 12"><path d="M7 0 L14 6 L12 6 L12 12 L8.5 12 L8.5 8 L5.5 8 L5.5 12 L2 12 L2 6 L0 6Z" fill="#fff"/></svg>Address: 742 Elm Row Marlowe, LA</div>
    <div><svg width="14" height="10" viewBox="0 0 14 10"><rect x=".5" y=".5" width="13" height="9" fill="none" stroke="#fff"/><path d="M.5 .5 L7 6 L13.5 .5" fill="none" stroke="#fff"/></svg>office@Wutbrand.de</div>
    <div><svg width="14" height="13" viewBox="0 0 14 13"><path d="M2 0 L5 0 L6 3 L4 5 Q6 8 9 9 L11 7 L14 8 L14 11 Q13 13 10 12 Q2 9 0 2 Q0 0 2 0Z" fill="#fff"/></svg>Cal us: ( 4120 ) 5530 918</div>
  </div>
  <div class="rule"></div>
  <div class="copy">Wutbrand.de 2013 Copyright.All rights Reserved!</div>
</footer>
</body>
</html>
```